Professional business cards for real estate development company

I need business cards for my new real estate development company. The company, "KORVA" is a real estate development, investment, and advisory firm with a focus on multifamily, office, and mixed-use projects across primary and secondary markets in the Southeast United States.

Style preference is modern

Industry/Entity Type

Real Estate Development

Contact Information for Business Card

The business cards need to include:
Name
Title
Mailing Address
Phone Number
Web Address

Logo is attached. I would like white to be the primary color with incorporation of the company colors: #232D3A and #B5A451

Font styles to use
Other font styles liked:
• Montserrat, Avenir

Requirements
Must have
• Company Logo. No need to include the company name since the name is in the logo.
Should not have
• No line type designs

```html
<!DOCTYPE html>
<html lang="en">
<head>
<meta charset="utf-8">
<title>KORVA Business Cards</title>
<link href="https://fonts.googleapis.com/css2?family=Montserrat:wght@400;500;600;700&display=swap" rel="stylesheet">
<style>
  :root {
    --canvas-bg: #e4e4e4;
    --card-bg: #f4f3ef;
    --navy: #232d3a;
    --gold: #b5a451;
    --card-shadow: 0 6px 14px rgba(0, 0, 0, 0.12);
  }
  * { margin: 0; padding: 0; box-sizing: border-box; }
  html, body {
    width: 1200px;
    height: 960px;
    overflow: hidden;
    background: var(--canvas-bg);
    font-family: "Montserrat", sans-serif;
  }
  .canvas {
    position: relative;
    width: 1200px;
    height: 960px;
  }
  .card {
    position: absolute;
    left: 397px;
    width: 412px;
    height: 236px;
    background: var(--card-bg);
    box-shadow: var(--card-shadow);
    color: var(--navy);
  }
  .card--front { top: 213px; }
  .card--back { top: 503px; }

  .brand {
    position: absolute;
    top: 78px;
    left: 0;
    right: 0;
    display: flex;
    justify-content: center;
    align-items: center;
    gap: 12px;
  }
  .brand__square {
    width: 18px;
    height: 18px;
    background: var(--navy);
  }
  .brand__name {
    font-size: 38px;
    font-weight: 600;
    letter-spacing: 3px;
    color: var(--navy);
    line-height: 1;
  }
  .front-web {
    position: absolute;
    top: 201px;
    left: 0;
    right: 0;
    text-align: center;
    font-size: 11.5px;
    font-weight: 600;
    letter-spacing: 1.2px;
    color: var(--gold);
  }

  .person {
    position: absolute;
    left: 43px;
    top: 53px;
  }
  .person__name {
    font-size: 18.5px;
    font-weight: 700;
    letter-spacing: 0.6px;
    line-height: 1;
  }
  .person__title {
    margin-top: 8px;
    font-size: 11px;
    font-weight: 500;
    letter-spacing: 1.6px;
    color: var(--gold);
  }
  .contact {
    position: absolute;
    left: 43px;
  }
  .contact--phone { top: 126px; }
  .contact--address { top: 167px; }
  .contact__label {
    font-size: 9.5px;
    font-weight: 500;
    letter-spacing: 1.3px;
    color: var(--gold);
    line-height: 1;
    margin-bottom: 4px;
  }
  .contact__value {
    font-size: 11.5px;
    font-weight: 500;
    line-height: 1.3;
  }
  .back-web {
    position: absolute;
    right: 20px;
    top: 193px;
    display: flex;
    align-items: center;
    gap: 12px;
    font-size: 11.5px;
    font-weight: 700;
    letter-spacing: 0.5px;
  }
  .back-web__bar {
    width: 3px;
    height: 12px;
    background: var(--gold);
  }
</style>
</head>
<body>
<main class="canvas">
  <section class="card card--front" aria-label="Card front">
    <div class="brand">
      <span class="brand__square"></span>
      <span class="brand__name">KORVA</span>
    </div>
    <p class="front-web">WWW.KORVA.COM</p>
  </section>

  <section class="card card--back" aria-label="Card back">
    <div class="person">
      <h1 class="person__name">NORA VALLEN</h1>
      <p class="person__title">DIRECTOR</p>
    </div>
    <div class="contact contact--phone">
      <p class="contact__label">PHONE</p>
      <p class="contact__value">555-302-4816x2040</p>
    </div>
    <div class="contact contact--address">
      <p class="contact__label">ADDRESS</p>
      <p class="contact__value">418 W HARBOR SUITE 120<br>LAKEVIEW, GA 30125</p>
    </div>
    <div class="back-web">
      <span class="back-web__bar"></span>
      <span>WWW.KORVA.COM</span>
    </div>
  </section>
</main>
</body>
</html>
```